New Letterhead request for our Law Firm!

We are a small Estate Planning Firm who just got out logo redesigned. It's attached. We need some letterhead for our client welcome letters and so forth. Clean, bright, and approachable is our style. If you need the specifications for our color scheme or other versions of the logo file, we have those too. Visit our website to get an idea about our services/aesthetics:https://bramblecove.law/

Target Market(s)

Adults 30-80

Colors

Designer to choose colors to be used in the design.

Requirements
Must have
• Logo with color. Contact information

```html
<!DOCTYPE html>
<html lang="en">
<head>
<meta charset="utf-8">
<title>Bramblecove Law Firm Letterhead</title>
<link rel="stylesheet" href="https://fonts.googleapis.com/css2?family=Open+Sans:wght@400;600;700&display=swap">
<style>
  :root {
    --backdrop: #cbcbcb;
    --paper: #fafafa;
    --sage: #779f87;
    --charcoal: #4a4a4c;
    --body-text: #666666;
    --ink-blue: #1f7fc0;
  }
  * { margin: 0; padding: 0; box-sizing: border-box; }
  html, body {
    width: 994px; height: 1200px; overflow: hidden;
    background: var(--backdrop);
    font-family: "Open Sans", Arial, sans-serif;
  }
  .letterhead {
    position: absolute; left: 196px; top: 175px;
    width: 601px; height: 851px;
    background: var(--paper);
    box-shadow: 0 0 2px rgba(0,0,0,0.08);
  }
  .brand {
    position: absolute; left: 190px; top: 52px;
    display: flex; align-items: center; gap: 10px;
  }
  .brand-mark {
    width: 62px; height: 62px; border-radius: 50%;
    border: 2px solid var(--sage);
  }
  .brand-name {
    color: var(--sage); font-weight: 700; line-height: 1.05;
  }
  .brand-name .firm { display: block; font-size: 24px; letter-spacing: 0.5px; }
  .brand-name .type { display: block; font-size: 13px; letter-spacing: 2.5px; }
  .letter {
    position: absolute; left: 60px; top: 207px; width: 481px;
    font-size: 8.9px; line-height: 15.3px; color: var(--body-text);
  }
  .salutation { margin-bottom: 30px; }
  .letter p.body { text-align: justify; margin-bottom: 15.3px; }
  .sign-off { position: absolute; left: 60px; top: 575px; color: var(--body-text); }
  .signer-label { font-size: 8.6px; font-weight: 700; }
  .signature {
    display: block; margin: 12px 0 10px;
    width: 146px; height: 30px;
    background: linear-gradient(90deg, rgba(31,127,192,0.18), rgba(31,127,192,0.08));
    border-radius: 3px;
  }
  .signer-role { font-size: 8.6px; }
  .contact-row {
    position: absolute; left: 0; right: 0; top: 776px;
    display: flex; justify-content: center; gap: 12px;
    font-size: 10.5px; color: var(--charcoal);
  }
  .contact-item { display: flex; align-items: center; gap: 6px; }
  .contact-item svg { width: 11px; height: 11px; }
  .address-band {
    position: absolute; left: 0; right: 0; top: 801px; height: 26px;
    background: linear-gradient(90deg, var(--sage) 0 50%, var(--charcoal) 50% 100%);
    color: #ffffff; font-size: 10.5px;
    display: flex; align-items: center; justify-content: center;
  }
</style>
</head>
<body>
  <main class="letterhead">
    <header class="brand">
      <span class="brand-mark"></span>
      <span class="brand-name">
        <span class="firm">BRAMBLECOVE</span>
        <span class="type">LAW FIRM</span>
      </span>
    </header>

    <section class="letter">
      <p class="salutation">Dear Sir,</p>
      <p class="body">Lorem Ipsum is simply dummy text of the printing and typesetting industry. Lorem Ipsum has been the industry's standard dummy text ever since the 1500s, when an unknown printer took a galley of type and scrambled it to make a type specimen book. It has survived not only five centuries, but also the leap into electronic typesetting, remaining essentially unchanged. It was popularised in the 1960s with the release of Typeleaf sheets containing Lorem Ipsum passages, and more recently with desktop publishing software like Pagecraft Studio including versions of Lorem Ipsum.</p>
      <p class="body">Lorem Ipsum is simply dummy text of the printing and typesetting industry. Lorem Ipsum has been the industry's standard dummy text ever since the 1500s, when an unknown printer took a galley of type and scrambled it to make a type specimen book. It has survived not only five centuries, but also the leap into electronic typesetting, remaining essentially unchanged. It was popularised in the 1960s with the release of Typeleaf sheets containing Lorem Ipsum passages, and more recently with desktop publishing software like Pagecraft Studio including versions of Lorem Ipsum.</p>
      <p class="body">Lorem Ipsum is simply dummy text of the printing and typesetting industry. Lorem Ipsum has been the industry's standard dummy text ever since the 1500s, when an unknown printer took a galley of type and scrambled it to make a type specimen book.</p>
    </section>

    <section class="sign-off">
      <p class="signer-label">Your Name</p>
      <span class="signature" role="img" aria-label="Handwritten signature of Daniel Morrow"></span>
      <p class="signer-role">CEO &nbsp;|&nbsp; Owner</p>
    </section>

    <footer>
      <div class="contact-row">
        <span class="contact-item">
          <svg viewBox="0 0 12 12" aria-hidden="true"><circle cx="6" cy="6" r="5.5" fill="none" stroke="#779f87"/><path d="M4 3.5 L5 3.5 L5.5 5 L4.9 5.5 Q5.5 6.8 6.6 7.2 L7.1 6.6 L8.5 7.1 L8.5 8.1 Q5 8.5 3.7 4.2 Z" fill="#779f87"/></svg>
          612 555 0148
        </span>
        <span class="contact-item">
          <svg viewBox="0 0 12 12" aria-hidden="true"><circle cx="6" cy="6" r="5.5" fill="none" stroke="#779f87"/><rect x="3.3" y="4.2" width="5.4" height="3.6" fill="none" stroke="#779f87" stroke-width="0.8"/><path d="M3.3 4.2 L6 6.2 L8.7 4.2" fill="none" stroke="#779f87" stroke-width="0.8"/></svg>
          info@bramblecove.law
        </span>
        <span class="contact-item">
          <svg viewBox="0 0 12 12" aria-hidden="true"><circle cx="6" cy="6" r="5.5" fill="none" stroke="#779f87"/><circle cx="6" cy="6" r="2.8" fill="none" stroke="#779f87" stroke-width="0.8"/><path d="M3.2 6 H8.8 M6 3.2 V8.8" stroke="#779f87" stroke-width="0.6"/></svg>
          www.bramblecove.law
        </span>
      </div>
      <div class="address-band">2400 Lakeview Parkway, Suite 310 Maple Grove, MN 55311</div>
    </footer>
  </main>
</body>
</html>
```